Business Card Design

I need business cards designed for a new company i have started that makes cakes, particularly themed kids cakes with a really modern design and I would like to have my business cards reflect this. I have attached some photos of cakes I have made and would like some to be used.

Industry/Entity Type

Business

Contact Information for Business Card

Business Name: Frosting and Treats by Norah
Mobile: 0427 519 863
email: norah@frostingandtreatsbynorah.com.au
Instagram: instagram.com/frostingandtreatsbynorah/
Facebook: fb.me/frostingandtreatsbynorah

Colors
e667a6
b768aa
3276b5

Requirements
Must have
• Business Name: Frosting and Treats by Norah
• Mobile: 0427 519 863
• email: norah@frostingandtreatsbynorah.com.au
• Instagram: instagram.com/frostingandtreatsbynorah/
• Facebook: fb.me/frostingandtreatsbynorah
Nice to have
• 2 to 3 pictures of my cakes

```html
<!DOCTYPE html>
<html lang="en">
<head>
<meta charset="utf-8">
<title>Frosting and Treats by Norah – Business Card</title>
<link href="https://fonts.googleapis.com/css2?family=Lato:wght@400;700&display=swap" rel="stylesheet">
<style>
  :root {
    --page-bg: #ebe9ea;
    --card-bg: #ffffff;
    --ink: #2f2f33;
    --pink: #e6509a;
    --ring: #ffffff;
    --shadow: rgba(60, 20, 40, 0.16);
    --photo-left: #cfcfcd;
    --photo-right: #d6d4cf;
    --feature-light: #ece8e2;
    --feature-deep: #cdbfae;
  }
  * { box-sizing: border-box; margin: 0; padding: 0; }
  html, body {
    width: 1200px;
    height: 863px;
    overflow: hidden;
    background: var(--page-bg);
    font-family: "Lato", Arial, sans-serif;
  }
  .stage {
    width: 1200px;
    height: 863px;
    display: flex;
    justify-content: center;
    align-items: center;
    gap: 60px;
  }
  .card {
    width: 320px;
    height: 525px;
    background: var(--card-bg);
    box-shadow: 0 10px 30px var(--shadow);
    position: relative;
    overflow: hidden;
  }

  /* Front */
  .card--front {
    display: flex;
    flex-direction: column;
    align-items: center;
    padding-top: 78px;
  }
  .brand {
    display: flex;
    flex-direction: column;
    align-items: center;
    gap: 14px;
  }
  .brand__dot {
    width: 14px;
    height: 14px;
    border-radius: 50%;
    background: var(--pink);
  }
  .brand__name {
    font-weight: 700;
    font-size: 17px;
    line-height: 1.45;
    letter-spacing: 0.14em;
    text-transform: uppercase;
    text-align: center;
    color: var(--ink);
  }
  .contact {
    list-style: none;
    margin-top: 78px;
    text-align: center;
    display: flex;
    flex-direction: column;
    gap: 15px;
  }
  .contact__label {
    display: block;
    font-size: 12px;
    color: var(--pink);
    margin-bottom: 2px;
  }
  .contact__value {
    display: block;
    font-size: 13px;
    color: var(--ink);
  }
  .contact__value--email { font-size: 11.5px; }

  /* Back */
  .gallery__photo {
    position: absolute;
    top: 26px;
    width: 136px;
    height: 230px;
  }
  .gallery__photo--left {
    left: 22px;
    background: linear-gradient(180deg, #dcdcda 0%, var(--photo-left) 100%);
  }
  .gallery__photo--right {
    left: 162px;
    background: linear-gradient(180deg, #e0dfdb 0%, var(--photo-right) 100%);
  }
  .gallery__feature {
    position: absolute;
    left: 12px;
    top: 212px;
    width: 296px;
    height: 296px;
    border-radius: 50%;
    border: 6px solid var(--ring);
    background: linear-gradient(180deg, var(--feature-light) 0%, var(--feature-deep) 100%);
  }
</style>
</head>
<body>
  <main class="stage">
    <section class="card card--front" aria-label="Business card front">
      <header class="brand">
        <span class="brand__dot" aria-hidden="true"></span>
        <h1 class="brand__name">Frosting and Treats<br>by Norah</h1>
      </header>
      <ul class="contact">
        <li>
          <span class="contact__label">Phone</span>
          <span class="contact__value">0427 519 863</span>
        </li>
        <li>
          <span class="contact__label">Instagram</span>
          <span class="contact__value">frostingandtreatsbynorah</span>
        </li>
        <li>
          <span class="contact__label">Facebook</span>
          <span class="contact__value">frostingandtreatsbynorah</span>
        </li>
        <li>
          <span class="contact__label">Email</span>
          <span class="contact__value contact__value--email">norah@frostingandtreatsbynorah.com.au</span>
        </li>
      </ul>
    </section>

    <section class="card card--back" aria-label="Business card back">
      <div class="gallery__photo gallery__photo--left" role="img" aria-label="Photo of a themed celebration cake"></div>
      <div class="gallery__photo gallery__photo--right" role="img" aria-label="Photo of a themed birthday cake"></div>
      <div class="gallery__feature" role="img" aria-label="Photo of a sliced layered birthday cake"></div>
    </section>
  </main>
</body>
</html>
```